Diagnose Krebs - Beratung für Ihre Klarheit
Schnelle und unkomplizierte Umsetzung. Die virtuelle Zusammenarbeit hat Spaß gemacht. Ich bin mit dem Ergebnis sehr zufrieden.
Zielgruppe
Für diesen besonderen Flyer gehören Krebspatienten zur Zielgruppe.
Aufgabenstellung
Dezentes Design, dennoch soll es Leichtigkeit und Lebenskraft ausstahlen - und sich abheben von schwer wirkenden Botschaften.
Ich habe Fotos von bildarnu gewählt, bin aber auch für Hinweise dankbar andere Designs zu wählen.
Am Text werde ich voraussichtlich noch Kürzungen vornehmen...ist das noch möglich?

```html
<!DOCTYPE html>
<html lang="de">
<head>
<meta charset="utf-8">
<title>Diagnose Krebs – Beratung für Ihre Klarheit</title>
<link href="https://fonts.googleapis.com/css2?family=Source+Sans+3:ital,wght@0,300;0,400;0,600;0,700;1,300;1,400&display=swap" rel="stylesheet">
<style>
  :root{
    --blue:#2b3591;
    --green:#a8c51b;
    --grey:#7b7b7b;
    --sky-light:#d9f0f3;
    --sky:#5cc3d3;
    --white:#ffffff;
  }
  *{margin:0;padding:0;box-sizing:border-box}
  html,body{width:1200px;height:613px;overflow:hidden;background:var(--white)}
  body{position:relative;font-family:"Source Sans 3",sans-serif;color:var(--grey)}
  .panel{position:absolute;top:66px;height:471px;background:var(--white);box-shadow:1px 2px 3px rgba(0,0,0,.35);overflow:hidden}
  .panel svg.bg{position:absolute;inset:0}
  .cover{left:88px;width:221px}
  .inside{left:378px;width:439px}
  .back{left:887px;width:221px}
  .abs{position:absolute}

  .brand-name{font-weight:400;color:var(--blue);letter-spacing:.5px}
  .brand-sub{font-weight:400;color:var(--blue);letter-spacing:.3px}

  .cover-title{left:17px;top:353px;color:var(--blue);font-weight:700;font-size:17px;line-height:24px}
  .cover-sub{left:17px;top:403px;color:var(--blue);font-size:10px}
  .cover .brand-name{right:18px;top:428px;font-size:13px}
  .cover .brand-sub{right:18px;top:451px;font-size:7px}

  .portrait{left:16px;top:16px;width:77px;height:103px}
  .name{left:99px;top:58px;color:var(--blue);font-weight:700;font-size:10.5px}
  .role{left:99px;top:71px;color:var(--blue);font-style:italic;font-weight:300;font-size:10.5px}
  .copy{font-size:6.6px;line-height:11px;text-align:justify;width:188px;left:16px;font-weight:400}
  .copy.intro{top:94px}
  .copy.intro .indent{display:block;padding-left:83px}
  .copy.accent{top:183px;color:var(--blue)}
  .copy.tail{top:271px}
  .call{left:16px;top:367px;width:200px;color:var(--blue);font-style:italic;font-size:8px;line-height:11px}
  .contact-small{left:16px;top:393px;font-style:italic;font-size:6px;line-height:9px;color:#9a9a9a}

  .col-head{left:236px;color:var(--blue);font-weight:300;font-size:10.5px;line-height:12.5px}
  .col-head.one{top:59px}
  .col-head.two{top:206px}
  .bullets{position:absolute;left:236px;width:195px;list-style:none;font-size:6.2px;line-height:9.5px}
  .bullets li{position:relative;padding-left:9px;margin-bottom:4.3px}
  .bullets li::before{content:"";position:absolute;left:0;top:3px;width:3.5px;height:3.5px;background:var(--blue)}
  .bullets.one{top:94px}
  .bullets.two{top:240px}

  .back .brand-name{left:22px;top:221px;font-size:13px}
  .back .brand-sub{left:23px;top:243px;font-size:8.5px}
  .company{left:16px;top:361px;color:var(--blue);font-size:8px}
  .address{top:376px;font-style:italic;font-weight:300;font-size:7.6px;line-height:12px;color:var(--grey)}
  .address.left{left:16px}
  .address.right{left:107px}
</style>
</head>
<body>

<!-- Titelseite -->
<section class="panel cover">
  <svg class="bg" width="221" height="471" viewBox="0 0 221 471">
    <defs>
      <linearGradient id="skyCover" x1="0" y1="0" x2="1" y2="1">
        <stop offset="0" stop-color="#bde6ec"/>
        <stop offset=".5" stop-color="#5fc4d4"/>
        <stop offset="1" stop-color="#e4f5f7"/>
      </linearGradient>
    </defs>
    <path role="img" aria-label="Foto: Pusteblumensamen vor türkisblauem Himmel" d="M0 0H221V290C160 330 80 345 0 344Z" fill="url(#skyCover)"/>
    <path d="M0 344C80 345 160 330 221 290V296C160 338 80 350 0 350Z" fill="var(--green)"/>
  </svg>
  <h1 class="abs cover-title">Diagnose Krebs<br>Beratung</h1>
  <p class="abs cover-sub">für Ihre Klarheit</p>
  <p class="abs brand-name">vitalkurs</p>
  <p class="abs brand-sub">health consulting</p>
</section>

<!-- Innenseite -->
<section class="panel inside">
  <svg class="bg" width="439" height="471" viewBox="0 0 439 471">
    <defs>
      <linearGradient id="sea" x1="0" y1="0" x2="0" y2="1">
        <stop offset="0" stop-color="#9fb8c8"/>
        <stop offset=".5" stop-color="#f2d9a8"/>
        <stop offset="1" stop-color="#7fa3b4"/>
      </linearGradient>
      <linearGradient id="leaf" x1="0" y1="0" x2="1" y2="1">
        <stop offset="0" stop-color="#8fc03a"/>
        <stop offset="1" stop-color="#3f7d1d"/>
      </linearGradient>
      <linearGradient id="notes" x1="0" y1="0" x2="1" y2="0">
        <stop offset="0" stop-color="#f2a531"/>
        <stop offset=".5" stop-color="#c9a6e3"/>
        <stop offset="1" stop-color="#7bd35a"/>
      </linearGradient>
    </defs>
    <path d="M0 50C90 48 190 25 240 0H222C170 22 90 40 0 43Z" fill="var(--green)"/>
    <path role="img" aria-label="Foto: bunte Notizzettel mit Frage- und Ausrufezeichen" d="M312 0H439V78C390 80 330 60 312 0Z" fill="url(#notes)"/>
    <path d="M312 0C330 60 390 80 439 78V82C385 84 325 64 306 0Z" fill="var(--green)"/>
    <path role="img" aria-label="Foto: Flaschenpost im Meer bei Sonnenuntergang" d="M8 471C70 420 140 395 220 393V471Z" fill="url(#sea)"/>
    <path role="img" aria-label="Foto: Ginkgoblätter mit Schild Lebensqualität" d="M220 393C320 392 400 420 439 445V471H220Z" fill="url(#leaf)"/>
    <path d="M0 471C60 415 140 388 220 388C320 388 400 415 439 440V445C400 420 320 393 220 393C140 395 70 420 8 471Z" fill="var(--green)"/>
  </svg>

  <div class="abs portrait" role="img" aria-label="Porträtfoto der Beraterin" style="background:linear-gradient(180deg,#a9b27c,#6f7852)"></div>
  <h2 class="abs name">Helena Varga</h2>
  <p class="abs role">Beratungsphilosophie</p>

  <p class="abs copy intro"><span class="indent">Durch die intensive eigene Erfahrung einer Brustkrebsdiagnose sowie die anspruchsvolle Gene-</span>sungsreise und die vielen Herausforderungen bin ich mit den körperlichen, seelischen und sozialen Themen rund um eine Krebserkrankung sehr vertraut. Jede Diagnose jedoch ist individuell, besonders und nie vergleichbar.</p>
  <p class="abs copy accent">Ich möchte mit meiner Art der Beratung die Erweiterung Ihrer eigenen Handlungsmöglichkeiten unterstützen, damit Sie für sich Klarheit und Lösungswege im Umgang mit Ihren Themen finden. Mein professioneller Hintergrund mit lösungsfokussiertem Coaching, energetischer Psychologie und systemischer Beratung bilden den Rahmen für die Arbeit mit Ihnen.</p>
  <p class="abs copy tail">Als außenstehende Beraterin höre ich zu, beobachte, stelle Fragen und beziehe den Körper als wichtige Ressource mit ein. Der Körper ist der vergessene Ort des Wissens, in dem Erfahrungen, Gefühle und Stimmungen abgespeichert sind und wertvolle Signale wahrnehmbar sind. Mit meiner hohen Sensibilität und einer Haltung der Nicht-Wissenden in Bezug auf Ihre Lösungen unterstütze ich Sie in Ihrer Selbstverantwortung.</p>
  <p class="abs call">Melden Sie sich gerne und wir schauen, ob und wie ich Sie unterstützen kann.</p>
  <p class="abs contact-small">0160 4821 7750<br>hv@vitalkurs-hc.de</p>

  <h2 class="abs col-head one">Folgende Gedanken<br>beschäftigen Sie…</h2>
  <ul class="bullets one">
    <li>Ich fühle mich orientierungslos und überfordert mit meiner Situation.</li>
    <li>Ich fühle mich unsicher Entscheidungen zu treffen.</li>
    <li>Wie gehe ich mit nahen Bezugspersonen um?</li>
    <li>Ängste rund um Wiedererkrankungen begleiten mich.</li>
    <li>Die Therapie ist abgeschlossen und nun stehe ich vor einem Berg an Fragen wie es weitergehen soll?</li>
    <li>Ich wünsche mir Raum für meine Fragen.</li>
  </ul>

  <h2 class="abs col-head two">Ziele der Beratung<br>können sein…</h2>
  <ul class="bullets two">
    <li>Die eigene Situation der Krebserkrankung annehmen lernen.</li>
    <li>Verankern von stärkenden Bildern für den Prozess.</li>
    <li>Körperwahrnehmung erhöhen und die Selbstheilungskräfte des Körpers aktivieren lernen.</li>
    <li>Lebensqualität steigern während und nach Abschluss von Therapiemaßnahmen.</li>
    <li>Selbstvertrauen und die eigene Entscheidungskompetenz stärken.</li>
    <li>Energieräuber und Kraftquellen bewusst wahrnehmen und danach handeln.</li>
    <li>Nahe Bezugspersonen in die Beratung einbeziehen.</li>
  </ul>
</section>

<!-- Rückseite -->
<section class="panel back">
  <svg class="bg" width="221" height="471" viewBox="0 0 221 471">
    <defs>
      <linearGradient id="skyBack" x1="0" y1="0" x2="1" y2="0">
        <stop offset="0" stop-color="#1f7fa8"/>
        <stop offset=".6" stop-color="#4fb8cf"/>
        <stop offset="1" stop-color="#d8eef2"/>
      </linearGradient>
    </defs>
    <path d="M0 290C60 268 140 265 221 272V278C140 272 60 276 0 296Z" fill="var(--green)"/>
    <path role="img" aria-label="Foto: Pusteblumensamen vor blauem Himmel" d="M0 296C60 276 140 272 221 278V350C140 350 60 335 0 346Z" fill="url(#skyBack)"/>
  </svg>
  <p class="abs brand-name">vitalkurs</p>
  <p class="abs brand-sub">health consulting</p>
  <p class="abs company">vitalkurs health consulting GmbH &amp; Co. KG</p>
  <p class="abs address left">Helena Varga<br>Birkenweg 5 – 7A<br>50931 Köln</p>
  <p class="abs address right">www.vitalkurs-hc.de<br>hv@vitalkurs-hc.de<br>tel. 0160 4821 7750</p>
</section>

</body>
</html>
```